Creative label for amber glass candle jar.

We are a candle company. Our products are handmade by us and natural. We are looking for something minimalistic and unique. We need a label for our candle jars (amber glass with black lid). Our current label doesn't match these requirements. We would like our products to be stocked in London shop, therefore design has to be up to a high standard. Jar specification Diameter (mm) 65 Height without cap (mm) 80. We want the new design to be different from the current one. It's just a guide for wording.
We should be able adjust the label, to change scent name.
Our scents are
*Coconut & Vanilla
*Lavender
*Bergamot
*Italian Garden
*Hygge
*Eucalyptus & Peppermint
*Coffee
*Cedarwood & Juniperberry
To know more about us, visit our website www.wrenfieldcandles.com or instagram.com/wrenfieldcandles
Good luck!
Industry/Entity Type
It Company
Colors
Designer to choose colors to be used in the design.
Requirements
Must have
- * I have attached two of our logos, label design must include one of them.
- *has to mention that it's made in London
- *has to say that candle is natural/made with essential oils
- *has to have scent name and No. on it..
- Label can be vertical or horizontal, but has to be square/rectangular,.
Should not have
- Label should not be round

```html
<!DOCTYPE html>
<html lang="en">
<head>
<meta charset="utf-8">
<title>Wrenfield Candle Labels</title>
<link href="https://fonts.googleapis.com/css2?family=Courier+Prime:wght@400;700&family=Homemade+Apple&display=swap" rel="stylesheet">
<style>
  :root {
    --paper: #ffffff;
    --ink: #1a1a1a;
    --rule: #2a2a2a;
    --backdrop: #ffffff;
    --coconut: #c8b99b;
    --lavender: #d3a3c8;
    --bergamot: #77c043;
    --italian: #5a5a5a;
    --eucalyptus: #1e9a47;
  }
  * { box-sizing: border-box; margin: 0; padding: 0; }
  html, body {
    width: 1200px; height: 867px; overflow: hidden;
    background: var(--backdrop);
  }
  .label-range {
    position: absolute;
    left: 56px; top: 366px;
    display: flex; gap: 22px;
  }
  .label {
    --accent: var(--coconut);
    position: relative;
    width: 200px; height: 136px;
    background: var(--paper);
    display: flex;
    box-shadow: 0 0 0 1px #e6e6e6;
    font-family: "Courier Prime", "Courier New", monospace;
    color: var(--ink);
  }
  .label--coconut { --accent: var(--coconut); }
  .label--lavender { --accent: var(--lavender); }
  .label--bergamot { --accent: var(--bergamot); }
  .label--italian { --accent: var(--italian); }
  .label--eucalyptus { --accent: var(--eucalyptus); }

  .brand-band {
    width: 32px; height: 100%;
    background: var(--accent);
    display: flex; align-items: center; justify-content: center;
  }
  .brand-name {
    writing-mode: vertical-rl;
    transform: rotate(180deg);
    font-size: 19px;
    letter-spacing: 3px;
    color: var(--ink);
  }
  .label--italian .brand-name,
  .label--eucalyptus .brand-name { color: #ffffff; }

  .label-body {
    position: relative;
    flex: 1;
    padding: 10px 8px 0 10px;
  }
  .top-rule {
    height: 1px; background: var(--rule);
    margin-left: 14px; margin-right: 4px;
  }
  .scent-name {
    height: 52px;
    display: flex; align-items: center;
    padding-left: 4px;
    font-size: 15.5px; line-height: 19px;
    letter-spacing: 0.3px;
  }
  .scent-name--single { padding-left: 12px; }
  .spec-row {
    position: relative;
    border-top: 1px solid var(--rule);
    border-bottom: 1px solid var(--rule);
    height: 13px;
    margin-left: 0; margin-right: 2px;
  }
  .spec-row::before {
    content: ""; position: absolute; left: 0; top: -1px;
    width: 1px; height: 14px; background: var(--rule);
  }
  .natural-tag {
    position: absolute; right: 0; top: 0; bottom: 0;
    width: 88px;
    border-left: 1px solid var(--rule);
    font-size: 8.5px; line-height: 12px;
    text-align: center;
  }
  .oils-row {
    position: relative;
    font-size: 6.5px; line-height: 9px;
    padding: 2px 0 0 0;
    border-bottom: 1px solid var(--rule);
    margin-right: 40px;
    height: 12px;
  }
  .oils-row::after {
    content: ""; position: absolute; right: 0; top: -1px;
    width: 1px; height: 12px; background: var(--rule);
  }
  .made-in {
    position: absolute; left: 12px; bottom: 6px;
    font-family: "Homemade Apple", cursive;
    font-size: 8px; color: #444;
  }
  .seal {
    position: absolute; right: 8px; bottom: 10px;
    width: 28px; height: 28px;
  }
</style>
</head>
<body>
<main class="label-range">

  <article class="label label--coconut">
    <div class="brand-band"><span class="brand-name">wrenfield</span></div>
    <div class="label-body">
      <div class="scent-name">Coconut<br>&amp; Vanilla</div>
      <div class="spec-row"><span class="natural-tag">Natural Candle</span></div>
      <div class="oils-row">made with essential oils</div>
      <p class="made-in">Made in London</p>
      <svg class="seal" viewBox="0 0 28 28" aria-hidden="true"><circle cx="14" cy="14" r="12.5" fill="none" stroke="var(--accent)" stroke-width="1.5"/><circle cx="14" cy="14" r="8" fill="var(--accent)" opacity="0.5"/></svg>
    </div>
  </article>

  <article class="label label--lavender">
    <div class="brand-band"><span class="brand-name">wrenfield</span></div>
    <div class="label-body">
      <div class="top-rule"></div>
      <div class="scent-name scent-name--single">Lavender</div>
      <div class="spec-row"><span class="natural-tag">Natural Candle</span></div>
      <div class="oils-row">made with essential oils</div>
      <p class="made-in">Made in London</p>
      <svg class="seal" viewBox="0 0 28 28" aria-hidden="true"><circle cx="14" cy="14" r="12.5" fill="none" stroke="var(--accent)" stroke-width="1.5"/><circle cx="14" cy="14" r="8" fill="var(--accent)" opacity="0.5"/></svg>
    </div>
  </article>

  <article class="label label--bergamot">
    <div class="brand-band"><span class="brand-name">wrenfield</span></div>
    <div class="label-body">
      <div class="top-rule"></div>
      <div class="scent-name scent-name--single">Bergamot</div>
      <div class="spec-row"><span class="natural-tag">Natural Candle</span></div>
      <div class="oils-row">made with essential oils</div>
      <p class="made-in">Made in London</p>
      <svg class="seal" viewBox="0 0 28 28" aria-hidden="true"><circle cx="14" cy="14" r="12.5" fill="none" stroke="var(--accent)" stroke-width="1.5"/><circle cx="14" cy="14" r="8" fill="var(--accent)" opacity="0.5"/></svg>
    </div>
  </article>

  <article class="label label--italian">
    <div class="brand-band"><span class="brand-name">wrenfield</span></div>
    <div class="label-body">
      <div class="top-rule"></div>
      <div class="scent-name scent-name--single">Italian<br>Garden</div>
      <div class="spec-row"><span class="natural-tag">Natural Candle</span></div>
      <div class="oils-row">made with essential oils</div>
      <p class="made-in">Made in London</p>
      <svg class="seal" viewBox="0 0 28 28" aria-hidden="true"><circle cx="14" cy="14" r="12.5" fill="none" stroke="#9a9a9a" stroke-width="1.5"/><circle cx="14" cy="14" r="8" fill="#9a9a9a" opacity="0.5"/></svg>
    </div>
  </article>

  <article class="label label--eucalyptus">
    <div class="brand-band"><span class="brand-name">wrenfield</span></div>
    <div class="label-body">
      <div class="top-rule"></div>
      <div class="scent-name" style="font-size:14px;">Eucalyptus<br>&amp; Peppermint</div>
      <div class="spec-row"><span class="natural-tag">Natural Candle</span></div>
      <div class="oils-row">made with essential oils</div>
      <p class="made-in">Made in London</p>
      <svg class="seal" viewBox="0 0 28 28" aria-hidden="true"><circle cx="14" cy="14" r="12.5" fill="none" stroke="var(--accent)" stroke-width="1.5"/><circle cx="14" cy="14" r="8" fill="var(--accent)" opacity="0.5"/></svg>
    </div>
  </article>

</main>
</body>
</html>
```